Take out menu for The Lantern Nook Café

I'd like to have my menu re imagined.
Menu: (see LanternNookCafe Current menu file)
- Using the "new menu" and "cater menu" files which are updated over the LanternNookCafe Current menu
- Should be able to fit onto 11 x 17 parallel fold design
- Similar to current menu with headings and menu descriptions
- I do not have a font preference, whatever you think looks great and is easily readable
- More creative layout
- No pics of real foods
- Keeping the colors in "Salad, Grill, Sandwich, etc"
- The Cover page needs to be more of a cover, with all the same information, just more creative layout using the new logo attached.
- Do not need the "Harborline Roasters" and "Bellavita" logos that are on the current menu..
- With the background colors I'd like to stay with either bright type of green to signify "fresh", bright yellow, sky blue and/or white.
- The ** menu items should be featured
- "LanternNookCafe Current Menu" cover has all the pertinent information that I would also like on the new menu. Front cover should include: Logo, address, phone, fax, email, hours, "Catering Trays Always Avaialable" "Visit thelanternnookcafe.com to see our weekly specials!" "Dine In, Take Out or Delivery" Facebook, Twitter, Instagram logos.
The above mentioned for the front cover do not need to be in that particular order.
- Prefer the logo to be over a white background always
- Back cover should have somewhere, maps shot (LNMap), "Free Parking" "Free Wireless" "Delivery Minimum $10"
- With the maps shot on back, please insert the logo where it currently says "The Lantern Nook Cafe"
The Lantern Nook Cafe is a breakfast and lunch cafe serving mostly corporate clientele. As the owner, I am laid back and whimsical and I'd like that to reflect in the designs. Nothing fancy or serious, that's not my intention with the design.
thelanternnookcafe.com
Any questions please ask. Thank you in advance to all the talented designers for working on my project, it is greatly appreciated!

```html
<!DOCTYPE html>
<html lang="en">
<head>
<meta charset="utf-8">
<title>The Lantern Nook Café – Catering Menu</title>
<link href="https://fonts.googleapis.com/css2?family=Fredoka:wght@500;600&family=Encode+Sans+Condensed:wght@400;600;700&display=swap" rel="stylesheet">
<style>
  :root {
    --red: #e4202a;
    --dark-red: #b3131c;
    --orange: #f26a21;
    --navy: #1f3f87;
    --purple: #7a4f96;
    --ink: #1a1a1a;
    --mint: #e6f3d6;
    --mint-deep: #d3ebbb;
    --sun-top: #fffbe0;
    --sun-bottom: #fde9a8;
    --sky-top: #ffffff;
    --sky-bottom: #a9d8f3;
    --white: #ffffff;
  }
  * { box-sizing: border-box; margin: 0; padding: 0; }
  html, body { width: 1200px; height: 780px; overflow: hidden; background: var(--white); }
  body { font-family: "Encode Sans Condensed", "Arial Narrow", sans-serif; color: var(--ink); }
  .menu { position: relative; width: 1200px; height: 780px; display: flex; overflow: hidden; }
  .panel { position: relative; width: 300px; height: 780px; padding: 0 22px 0 30px; font-size: 10.4px; line-height: 11.7px; overflow: hidden; }
  .panel--catering { background: linear-gradient(180deg, var(--mint), var(--mint-deep)); }
  .panel--lunch { background: linear-gradient(180deg, var(--sun-top), var(--sun-bottom)); }
  .panel--themed { background: linear-gradient(180deg, var(--mint), var(--mint-deep)); }
  .panel--cover { background: linear-gradient(180deg, var(--sky-top) 0%, var(--sky-top) 34%, var(--sky-bottom) 100%); padding: 0 18px; text-align: center; }

  .kicker { font-family: "Fredoka", sans-serif; font-weight: 600; color: var(--red); font-size: 22px; line-height: 26px; letter-spacing: 5px; text-align: center; margin-top: 24px; }
  .pill { display: block; margin: 6px auto 12px; width: 190px; height: 32px; border-radius: 50%; color: var(--white);
          font-family: "Fredoka", sans-serif; font-weight: 600; font-size: 16px; line-height: 32px; text-align: center; letter-spacing: .5px; }
  .pill--orange { background: var(--orange); margin: 10px auto 14px; }
  .pill--navy { background: var(--navy); margin-top: 34px; width: 196px; }
  .pill--red { background: var(--dark-red); margin-top: 34px; width: 196px; margin-bottom: 10px; }
  .pill--dessert { background: var(--orange); width: 246px; margin: 12px auto 10px; }
  .pill--policy { background: var(--purple); width: 196px; margin: 14px auto 12px; }

  .item { margin-bottom: 8px; }
  .item__title { font-weight: 700; font-size: 11.2px; line-height: 12.5px; }
  .panel--catering .item__title { color: var(--orange); }
  .panel--lunch .item__title { color: var(--navy); }
  .panel--themed .item__title { color: var(--dark-red); }
  .panel--themed .group .item__title { color: var(--orange); }
  .price { font-weight: 700; }
  .label { font-weight: 700; }
  .sub { color: var(--dark-red); }
  .panel--lunch .sub { color: var(--navy); font-weight: 700; }
  .panel--catering .sub { color: var(--orange); font-weight: 700; }

  ul.list { list-style: none; padding-left: 20px; }
  ul.list li { position: relative; padding-left: 12px; }
  ul.list li::before { content: "•"; position: absolute; left: 0; top: 0; color: var(--navy); }
  .panel--catering ul.list li::before { color: var(--orange); }
  .panel--themed ul.list li::before { color: var(--red); }
  ul.list--ink li::before { color: var(--ink) !important; }
  ul.list--orange li::before { color: var(--orange) !important; }
  ul.list--purple { padding-left: 0; font-size: 9.6px; line-height: 11px; }
  ul.list--purple li::before { color: var(--purple) !important; }

  .perks { font-weight: 700; font-size: 12px; margin: 10px 0 10px; white-space: nowrap; }
  .perks .dot { color: var(--red); margin: 0 5px; }
  .map { display: block; width: 193px; height: 190px; margin-left: 23px; border: 5px solid var(--red); background: linear-gradient(160deg, #f4f4f4, #e3e3ea); }
  .mail-box { position: absolute; left: 28px; top: 672px; width: 244px; height: 78px; border: 1.5px solid var(--ink); background: var(--white); }

  .brand { margin: 66px auto 0; width: 250px; height: 150px; background: var(--white); display: flex; align-items: center; justify-content: center; gap: 10px; }
  .brand__dot { width: 16px; height: 16px; border-radius: 50%; background: var(--red); flex: none; }
  .brand__name { font-family: "Fredoka", sans-serif; font-weight: 600; color: var(--red); font-size: 30px; line-height: 32px; text-align: left; }
  .taglines { margin-top: 80px; }
  .tagline { font-family: "Fredoka", sans-serif; font-weight: 600; color: var(--red); font-size: 17px; line-height: 19px; margin-bottom: 17px; }
  .info { font-size: 10.4px; line-height: 12px; margin-bottom: 13px; }
  .info strong { font-weight: 700; }
  .info--phone { font-size: 12px; line-height: 14px; }
  .cta { font-family: "Fredoka", sans-serif; font-weight: 600; color: var(--red); font-size: 17px; line-height: 19px; margin-top: 26px; }
  .social { display: flex; justify-content: center; gap: 26px; margin-top: 40px; }
  .social__square { width: 46px; height: 46px; background: var(--white); border: 2px solid var(--navy); border-radius: 6px; }
</style>
</head>
<body>
<main class="menu">

  <section class="panel panel--catering">
    <h1 class="kicker">CATERING</h1>
    <h2 class="pill pill--orange">BREAKFAST</h2>

    <div class="item">
      <div class="item__title">Bagel Tray</div>
      Includes cream cheese, butter, grape jelly and a selection of fresh bagels — <span class="price">2.00/guest</span>
    </div>
    <div class="item">
      <div class="item__title">Baked Goods Tray</div>
      Danishes, croissants, muffins and scones with butter and grape jelly — <span class="price">2.00/guest</span>
    </div>
    <div class="item">
      <div class="item__title">Breakfast Sandwich Tray</div>
      — <span class="price">3.50/guest</span><br>
      Includes egg, cheese, assorted meats and choice of bread
      <ul class="list">
        <li><span class="label">Bread</span> (choose one) bagel English muffin or kaiser</li>
        <li><span class="label">Cheese</span> (choose one) American, cheddar or Swiss</li>
        <li><span class="label">Meat</span> (choose from) bacon, sausage, ham, turkey sausage or pork roll</li>
      </ul>
      <span class="sub">Add home fries</span> — <span class="price">1.00/guest</span>
    </div>
    <div class="item">
      <div class="item__title">Breakfast Burrito Tray</div>
      Burritos include eggs, shredded cheese, salsa, choice of meat, onions and peppers wrapped in a flour tortilla and grilled — <span class="price">4.25/guest</span>
    </div>
    <div class="item">
      <div class="item__title">Breakfast Box</div>
      Includes bagel with cream cheese or one pastry (danish, croissant, muffin or scone), yogurt and fruit cup — <span class="price">5.95/guest</span>
    </div>
    <div class="item">
      <div class="item__title">Deluxe Breakfast Buffet Bar</div>
      Includes scrambled eggs, home fries, French toast and choice of one meat and fruit salad — <span class="price">6.50/guest</span>
    </div>

    <p class="perks">Free Parking<span class="dot">•</span>Free Wireless<span class="dot">•</span>Delivery Minimum $10</p>
    <div class="map" role="img" aria-label="Street map showing the route to The Lantern Nook Café in the commerce center, with the café name marking its spot"></div>
    <div class="mail-box"></div>
  </section>

  <section class="panel panel--lunch">
    <h2 class="pill pill--navy">LUNCH</h2>

    <div class="item">
      <div class="item__title">Cold Sandwich or Wrap Tray</div>
      Choose from a selection of sandwich options.<br>
      Includes pickles, condiments and chips.<br>
      Served on an assortment of rolls and wraps — <span class="price">7.00/guest</span><br>
      <span class="sub">(choose up to six)</span>
      <ul class="list">
        <li>Home cooked turkey</li><li>Home cooked roast beef</li><li>Tavern ham</li><li>Italian</li>
        <li>Tuna salad</li><li>Chicken salad</li><li>Egg salad</li><li>Mediterranean</li>
        <li>Buffalo chicken (wrap only)</li><li>Chicken Caesar (wrap only)</li>
        <li>Veggie avocado (vegetarian)</li><li>Tomato, mozz &amp; spinach (vegetarian)</li>
      </ul>
    </div>
    <div class="item" style="margin-top:14px">
      <div class="item__title">Hot Sandwich Tray</div>
      Choose from a selection of paninis, melts, wraps and sandwiches. Includes pickles, condiments and chips. Served on an assortment of rolls and wraps — <span class="price">7.00/guest</span><br>
      <span class="sub">(choose up to six)</span>
      <ul class="list">
        <li>BBQ chicken</li><li>Chicken fajita</li><li>Chicken mozzarella</li><li>Cajun chicken</li>
        <li>Commerce chicken</li><li>Cordon bleu</li><li>Reuben (turkey, roast beef or ham)</li>
        <li>Tuna melt</li><li>Roast beef &amp; bleu</li><li>Veggie (vegetarian)</li><li>Caprese (vegetarian)</li>
      </ul>
    </div>
    <div class="item" style="margin-top:12px">
      <div class="item__title">Add side salad — <span class="price">1.25/guest</span></div>
      <ul class="list">
        <li>Garden with balsamic vinaigrette</li><li>Caesar</li><li>Mediterranean</li><li>Pasta salad</li>
      </ul>
    </div>
    <div class="item" style="margin-top:10px">
      <div class="item__title">Sandwich Lunch Boxes</div>
      Choice of sandwich or wrap, an apple, two cookies and choice of side salad — <span class="price">9.00/guest</span><br>
      <span class="sub">Choose one sandwich:</span>
      <ul class="list">
        <li>Home cooked turkey</li><li>Home cooked roast beef</li><li>Italian</li><li>Ham &amp; cheese</li>
        <li>Tuna, chicken or egg salad</li><li>Veggie avocado (vegetarian)</li>
      </ul>
    </div>
    <div class="item" style="margin-top:10px">
      <div class="item__title">Choose side salad:</div>
      <ul class="list">
        <li>Garden with balsamic vinaigrette</li><li>Caesar</li><li>Mediterranean</li><li>Pasta salad</li>
      </ul>
    </div>
  </section>

  <section class="panel panel--themed">
    <h2 class="pill pill--red">THEMED LUNCHES</h2>

    <div class="item">
      <div class="item__title">Italiano</div>
      Choice of one Italian entrée paired with a pasta dish. Includes your choice of classic garden or Caesar salad with rolls and butter and mini cannoli — <span class="price">10.00/guest</span><br>
      <span class="sub">Entrées</span> (choose one)
      <ul class="list">
        <li>Chicken parmesan</li><li>Meatballs with sausage in sauce</li>
        <li>Chicken with sautéed spinach, sun-dried tomatoes and mozzarella cheese</li>
      </ul>
      <span class="sub">Pasta</span> (choose one)
      <ul class="list">
        <li>Spaghetti with sauce (tomato or alfredo)</li><li>Meatless lasagna</li><li>Baked ziti</li><li>Ravioli</li>
      </ul>
    </div>
    <div class="item">
      <div class="item__title">A Taste of Philly</div>
      Includes mini cheesesteaks, mini Italian hoagies, Crisply's potato chips, and soft pretzels bites — <span class="price">9.50/guest</span>
    </div>
    <div class="item">
      <div class="item__title">Classic American</div>
      Hot home cooked sliced turkey with gravy, hot home cooked roast beef in au jus, assorted rolls, pickles, coleslaw, chips, mini fresh baked cookies and condiments — <span class="price">9.50/guest</span>
    </div>
    <div class="item">
      <div class="item__title">Taco Party</div>
      Seasoned ground beef, seasoned pulled chicken, hard and soft tortillas, cheese, lettuce, tomato, sour cream, salsa and guacamole with tortilla chips — <span class="price">9.00/guest</span>
    </div>

    <h2 class="pill pill--dessert">DESSERTS &amp; BEVERAGES</h2>
    <div class="group">
      <div class="item">
        <div class="item__title">Desserts</div>
        <ul class="list list--ink">
          <li>Assorted cookie and brownie tray — <span class="price">1.25/guest</span></li>
          <li>Assorted pastry tray — <span class="price">1.50/guest</span></li>
          <li>Fruit tray — <span class="price">1.50/guest</span></li>
        </ul>
      </div>
      <div class="item">
        <div class="item__title">Beverages</div>
        <ul class="list list--orange">
          <li>Coffee station includes choice of coffee and cream <span class="sub" style="color:var(--orange)">Airpot</span> — <span class="price">8.00 (holds 7 12oz cups)</span></li>
          <li>Bottled water &amp; assorted juices (cranberry, orange and apple) — <span class="price">1.50/guest</span></li>
          <li>Assorted soda and iced tea bottles — <span class="price">1.75/guest</span></li>
          <li>Assorted soda and iced tea cans — <span class="price">1.00/guest</span></li>
        </ul>
      </div>
      <div class="item">
        <div class="item__title">All Orders Include:</div>
        Disposable utensils, cups, napkins and plates
      </div>
    </div>

    <h2 class="pill pill--policy">CATERING POLICIES</h2>
    <ul class="list list--purple">
      <li>Please provide 24 hours notice on all orders</li>
      <li>A delivery charge applies to deliveries</li>
      <li>We require 24 hours notice on all cancellations. Less than 24 hours notice will be subject to a 50% fee</li>
      <li>Pricing and offerings are subject to change</li>
      <li>Minimum 6 per order</li>
      <li>We accept cash, check and all major credit cards</li>
    </ul>
  </section>

  <section class="panel panel--cover">
    <div class="brand">
      <span class="brand__dot"></span>
      <span class="brand__name">The Lantern<br>Nook Café</span>
    </div>

    <div class="taglines">
      <p class="tagline">Dine In, Take Out or Delivery</p>
      <p class="tagline">Serving Breakfast and Lunch</p>
      <p class="tagline">Catering Trays always<br>available</p>
    </div>

    <p class="info" style="margin-top:34px"><strong>Monday through Friday</strong> 7:15am to 2:15pm</p>
    <p class="info"><strong>Located at:</strong><br>The Brookfield Commerce Center<br>N. Meadow Rd., Suite 210<br>Brookfield, PA 18970</p>
    <p class="info info--phone"><strong>Phone:</strong> 555-014-2286<br><strong>Fax:</strong> 555-014-2287</p>
    <p class="info info--phone"><strong>Email:</strong> hello@lanternnookcafe.net</p>

    <p class="cta">Visit thelanternnookcafe.com<br>to see our<br>weekly specials!</p>

    <div class="social" aria-label="Social media links">
      <span class="social__square"></span>
      <span class="social__square"></span>
      <span class="social__square"></span>
    </div>
  </section>

</main>
</body>
</html>
```